New Web Design for Clothing Store

We want to have a video section.

A place to showcase new items.

We have provided a copy of the logo.

All creative ideas are welcome.

```html
<!DOCTYPE html>
<html lang="en">
<head>
<meta charset="utf-8">
<title>Velmore – Clothing Store</title>
<link href="https://fonts.googleapis.com/css2?family=Outfit:wght@500;600;700&family=Montserrat:wght@400;500;600;700&display=swap" rel="stylesheet">
<style>
  :root {
    --ink: #000000;
    --paper: #ffffff;
    --text-dark: #111111;
    --text-muted: #6b6b6b;
    --star-on: #e5ad17;
    --star-off: #d9d9d9;
    --sale: #ef5b5b;
    --play: #e0484a;
    --hairline: #2a2a2a;
  }
  * { margin: 0; padding: 0; box-sizing: border-box; }
  html, body { width: 709px; height: 1200px; overflow: hidden; background: var(--paper); }
  body { position: relative; font-family: "Montserrat", sans-serif; color: var(--text-dark); }

  .site-header { position: absolute; left: 0; top: 0; width: 709px; height: 63px; background: var(--ink); border-bottom: 1px solid var(--hairline); }
  .menu-toggle { position: absolute; left: 71px; top: 29px; width: 25px; height: 16px; }
  .brand { position: absolute; display: flex; align-items: center; gap: 5px; color: var(--paper); font-family: "Outfit", sans-serif; font-weight: 600; letter-spacing: 1px; }
  .site-header .brand { left: 118px; top: 26px; font-size: 17px; }
  .brand-mark { width: 7px; height: 7px; background: var(--paper); }
  .search { position: absolute; left: 255px; top: 28px; width: 215px; height: 21px; border: 1px solid #8a8a8a; border-radius: 11px; display: flex; align-items: center; padding-left: 9px; gap: 6px; font-size: 6.5px; color: #bdbdbd; }
  .header-icon { position: absolute; top: 32px; width: 13px; height: 13px; }
  .icon-account { left: 589px; }
  .icon-cart { left: 622px; }

  .hero { position: absolute; left: 0; top: 63px; width: 709px; height: 311px; background: var(--ink); }
  .hero-title { position: absolute; left: 73px; top: 60px; color: var(--paper); font-family: "Outfit", sans-serif; font-weight: 600; font-size: 23px; line-height: 29px; }
  .hero-text { position: absolute; left: 73px; top: 134px; width: 310px; color: #e6e6e6; font-size: 9.6px; line-height: 12px; }
  .btn-read { position: absolute; left: 73px; top: 210px; width: 86px; height: 26px; background: var(--paper); border-radius: 2px; font-size: 8.5px; font-weight: 500; display: flex; align-items: center; justify-content: center; color: var(--text-dark); }
  .hero-video { position: absolute; left: 405px; top: 0; width: 304px; height: 311px; background: radial-gradient(ellipse at 60% 55%, #3a3a2e 0%, #26281f 45%, #15170f 100%); }
  .play-btn { position: absolute; left: 141px; top: 130px; width: 38px; height: 38px; }
  .slider-dots { position: absolute; left: 143px; top: 294px; display: flex; gap: 3px; }
  .slider-dots span { width: 4px; height: 4px; border-radius: 50%; background: #9a9a9a; }
  .slider-dots span.active { background: var(--paper); }

  .section-title { position: absolute; left: 73px; top: 428px; font-family: "Outfit", sans-serif; font-weight: 600; font-size: 16px; }

  .product { position: absolute; width: 180px; text-align: center; }
  .product-photo { position: relative; width: 180px; height: 182px; }
  .photo-scarf { background: linear-gradient(135deg, #f2f2f0 0%, #e9e6d6 45%, #d8d49a 70%, #eeeeea 100%); }
  .photo-street { background: linear-gradient(180deg, #8c9a86 0%, #6f7a72 40%, #8a8a8c 75%, #a09a90 100%); }
  .photo-denim { background: linear-gradient(160deg, #a9b4b6 0%, #9aa8ad 50%, #7e8f9c 100%); }
  .badge-sale { position: absolute; left: 0; top: 15px; background: var(--sale); color: var(--paper); font-size: 6px; padding: 1px 4px; }
  .wish { position: absolute; right: 9px; top: 11px; width: 10px; height: 9px; }
  .stars { margin-top: 9px; font-size: 11px; letter-spacing: 4px; line-height: 12px; color: var(--star-off); }
  .stars .on { color: var(--star-on); }
  .product-name { margin-top: 4px; font-size: 9.5px; color: var(--text-muted); line-height: 12px; }
  .product-price { margin-top: 5px; font-size: 11.5px; font-weight: 700; line-height: 14px; }
  .product-cta { margin-top: 5px; font-size: 9.5px; font-weight: 500; line-height: 14px; }

  .col-1 { left: 73px; } .col-2 { left: 265px; } .col-3 { left: 456px; }
  .row-1 { top: 463px; } .row-2 { top: 718px; }

  .site-footer { position: absolute; left: 0; top: 1027px; width: 709px; height: 173px; background: var(--ink); color: var(--paper); }
  .site-footer .brand { left: 73px; top: 50px; font-size: 17px; }
  .footer-about { position: absolute; left: 73px; top: 91px; width: 170px; font-size: 9.8px; line-height: 11.5px; color: #e6e6e6; }
  .footer-col { position: absolute; top: 62px; }
  .footer-col h4 { font-size: 8.8px; font-weight: 500; letter-spacing: 0.3px; margin-bottom: 9px; }
  .footer-col li { list-style: none; font-size: 7.6px; line-height: 17px; }
  .col-assist { left: 279px; } .col-help { left: 387px; } .col-unite { left: 477px; }
  .social { display: flex; gap: 10px; margin-top: 2px; }
  .social span { width: 10px; height: 10px; border-radius: 50%; border: 1.2px solid var(--paper); }
</style>
</head>
<body>

<header class="site-header">
  <svg class="menu-toggle" viewBox="0 0 25 16" aria-label="Menu"><path d="M0 1h25M0 8h20M0 15h25" stroke="#fff" stroke-width="1.3"/></svg>
  <div class="brand"><span class="brand-mark"></span>VELMORE</div>
  <div class="search">
    <svg width="8" height="8" viewBox="0 0 8 8"><circle cx="3.4" cy="3.4" r="2.6" fill="none" stroke="#bbb" stroke-width="0.9"/><path d="M5.4 5.4l2 2" stroke="#bbb" stroke-width="0.9"/></svg>
    search your item
  </div>
  <svg class="header-icon icon-account" viewBox="0 0 13 13" aria-label="Account"><circle cx="6.5" cy="4" r="2.6" fill="none" stroke="#fff" stroke-width="1.2"/><path d="M2 12c0-3 2-4.5 4.5-4.5S11 9 11 12" fill="none" stroke="#fff" stroke-width="1.2"/></svg>
  <svg class="header-icon icon-cart" viewBox="0 0 13 13" aria-label="Cart"><rect x="1.5" y="3.5" width="10" height="8.5" rx="1.5" fill="none" stroke="#fff" stroke-width="1.2"/><path d="M4.5 5.5V3a2 2 0 0 1 4 0v2.5" fill="none" stroke="#fff" stroke-width="1.2"/></svg>
</header>

<section class="hero">
  <h1 class="hero-title">Stylish Female<br>Clothes</h1>
  <p class="hero-text">Lorem ipsum dolor sit amet, consectetur adipiscing elit. Elit lorem non vitae, praesent aliquam dignissim enim, vulputate platea. Scelerisque felis, et eget risus egestas cursus</p>
  <a class="btn-read">Read More</a>
  <div class="hero-video" role="img" aria-label="Video still of a woman in a long floral dress standing in a dim old courtyard">
    <svg class="play-btn" viewBox="0 0 38 38" aria-label="Play video"><circle cx="19" cy="19" r="19" fill="var(--play)"/><path d="M15 12l11 7-11 7z" fill="#fff"/></svg>
    <div class="slider-dots"><span class="active"></span><span></span><span></span></div>
  </div>
</section>

<h2 class="section-title">Featured Product</h2>

<article class="product col-1 row-1">
  <div class="product-photo photo-scarf" role="img" aria-label="Patterned yellow scarf with sunglasses and palm leaf"></div>
  <div class="stars"><span class="on">★★★</span>★★</div>
  <p class="product-name">Lorem Good Product</p>
  <p class="product-price">$40.00</p>
</article>
<article class="product col-2 row-1">
  <div class="product-photo photo-street" role="img" aria-label="Man in teal jacket seated on a street post"><span class="badge-sale">Sale</span></div>
  <div class="stars"><span class="on">★★★★</span>★</div>
  <p class="product-name">Lorem Good Product</p>
  <p class="product-cta">Add To Cart</p>
</article>
<article class="product col-3 row-1">
  <div class="product-photo photo-denim" role="img" aria-label="Woman in a denim jacket against a pale wall">
    <svg class="wish" viewBox="0 0 10 9" aria-label="Wishlist"><path d="M5 9L1 5A2.3 2.3 0 0 1 5 1.6 2.3 2.3 0 0 1 9 5z" fill="#fff"/></svg>
  </div>
  <div class="stars"><span class="on">★★</span>★★★</div>
  <p class="product-name">Lorem Good Product</p>
  <p class="product-price">$40.00</p>
</article>

<article class="product col-1 row-2">
  <div class="product-photo photo-scarf" role="img" aria-label="Patterned yellow scarf with sunglasses and palm leaf"><span class="badge-sale">Sale</span></div>
  <div class="stars"><span class="on">★★★</span>★★</div>
  <p class="product-name">Lorem Good Product</p>
  <p class="product-price">$40.00</p>
</article>
<article class="product col-2 row-2">
  <div class="product-photo photo-street" role="img" aria-label="Man in teal jacket seated on a street post">
    <svg class="wish" viewBox="0 0 10 9" aria-label="Wishlist"><path d="M5 9L1 5A2.3 2.3 0 0 1 5 1.6 2.3 2.3 0 0 1 9 5z" fill="#fff"/></svg>
  </div>
  <div class="stars"><span class="on">★★★</span>★★</div>
  <p class="product-name">Lorem Good Product</p>
  <p class="product-price">$40.00</p>
</article>
<article class="product col-3 row-2">
  <div class="product-photo photo-denim" role="img" aria-label="Woman in a denim jacket against a pale wall"><span class="badge-sale">Sale</span></div>
  <div class="stars"><span class="on">★★★★</span>★</div>
  <p class="product-name">Lorem Good Product</p>
  <p class="product-price">$40.00</p>
</article>

<footer class="site-footer">
  <div class="brand"><span class="brand-mark"></span>VELMORE</div>
  <p class="footer-about">Lorem ipsum dolor sit amet, consectetur adipiscing elit. Elit lorem non vitae, praesent aliquam dignissim enim,</p>
  <div class="footer-col col-assist">
    <h4>ASSIST</h4>
    <ul><li>Order Statue</li><li>Shipping</li><li>Feature</li><li>Affiliate</li><li>Fit Guide</li></ul>
  </div>
  <div class="footer-col col-help">
    <h4>HELP</h4>
    <ul><li>Contact</li><li>Sitemap</li></ul>
  </div>
  <div class="footer-col col-unite">
    <h4>UNITE</h4>
    <div class="social"><span aria-label="Social link"></span><span aria-label="Social link"></span><span aria-label="Social link"></span><span aria-label="Social link"></span></div>
  </div>
</footer>

</body>
</html>
```